Signage Design Project

We are a chiropractic clinic that caters mostly to athletes. We've recently purchased the first whole body cryotherapy unit in San Antonio, TX (for commercial use - the SA Comets have a unit for their facility) that we would like to advertise in window signage. Please refer to frostvale.com & chillharbor.com to get more info about this service. Our focus is recovery, injury therapy, performance enhancement, metabolic & immunity boost, rheumatoid diseases & pain management, anti-aging & skin rejuvenation. Window measures approximately 8'8" X 3'2"
We mostly use the horizontal logo format (attached) in black & blue.
Industry/Entity Type
Clinic
Requirements
Must have
- Website: www.kelworthback.com
Logo (attached)
"JUST 3 MINUTES FOR WHOLE BODY RECOVERY"
"Whole Body Cryotherapy"
*recovery
*injury therapy
*performance enhancement
*metabolic & immunity boost
*rheumatoid diseases
*pain management
*anti-aging
*skin rejuvenation
Nice to have
- image of Cryo unit (attached)
image of an athlete(s) similar to the ones attached

```html
<!DOCTYPE html>
<html lang="en">
<head>
<meta charset="utf-8">
<title>Whole Body Cryotherapy – Window Sign</title>
<link rel="stylesheet" href="https://fonts.googleapis.com/css2?family=Anton&family=Archivo+Black&family=Oswald:wght@500;700&display=swap">
<style>
  :root {
    --ink: #0a0a0a;
    --paper: #ffffff;
    --brand-blue: #2b8fd8;
    --brand-blue-deep: #1f78c4;
    --brand-blue-light: #45a6ea;
    --unit-dark: #4a4f55;
    --unit-light: #c9ced3;
  }
  * { margin: 0; padding: 0; box-sizing: border-box; }
  html, body { width: 1200px; height: 2937px; overflow: hidden; background: var(--paper); }
  .sign {
    position: relative;
    width: 1200px;
    height: 2937px;
    overflow: hidden;
    background: var(--paper);
    font-family: "Oswald", "Arial Narrow", sans-serif;
    color: var(--ink);
  }
  .headline {
    position: absolute;
    top: 40px;
    left: 0;
    width: 1200px;
    text-align: center;
    font-family: "Archivo Black", "Arial Black", sans-serif;
    font-weight: 400;
    font-size: 200px;
    line-height: 168px;
    letter-spacing: -6px;
    color: var(--ink);
  }
  .banner {
    position: absolute;
    top: 406px;
    left: 46px;
    width: 1108px;
    height: 130px;
    background: linear-gradient(180deg, var(--brand-blue-light), var(--brand-blue-deep));
    display: flex;
    align-items: center;
    justify-content: center;
    font-family: "Archivo Black", "Arial Black", sans-serif;
    font-size: 112px;
    letter-spacing: -2px;
    color: var(--paper);
  }
  .benefits {
    position: absolute;
    top: 580px;
    left: 140px;
    list-style: none;
  }
  .benefits li {
    display: flex;
    align-items: center;
    height: 86px;
    font-weight: 700;
    font-size: 62px;
    text-transform: uppercase;
    transform: skewX(-6deg) rotate(-1.5deg);
    transform-origin: left center;
  }
  .benefits li::before {
    content: "";
    flex: none;
    width: 44px;
    height: 44px;
    margin-right: 26px;
    background: var(--ink);
  }
  .benefits li.alt { color: var(--brand-blue-light); }
  .benefits li.alt::before { background: var(--brand-blue-light); }
  .unit-visual {
    position: absolute;
    top: 1300px;
    left: 240px;
    width: 760px;
    height: 1400px;
    border-radius: 40px 40px 10px 10px;
    background: linear-gradient(90deg, var(--unit-dark) 0%, var(--unit-light) 45%, var(--unit-dark) 100%);
  }
  .offer {
    position: absolute;
    top: 1840px;
    left: 40px;
    width: 660px;
    height: 560px;
    background: var(--brand-blue);
    color: var(--paper);
    font-family: "Anton", Impact, sans-serif;
    padding: 30px 0 0 40px;
    transform: rotate(-3deg);
    transform-origin: left top;
  }
  .offer .just { font-size: 96px; line-height: 100px; }
  .offer .count {
    display: grid;
    grid-template-columns: auto 1fr;
    align-items: end;
    column-gap: 10px;
  }
  .offer .digit { font-size: 230px; line-height: 200px; grid-row: 1 / span 2; }
  .offer .minutes { font-size: 112px; line-height: 112px; }
  .offer .for { font-size: 52px; line-height: 60px; padding-left: 120px; }
  .offer .tail { font-size: 84px; line-height: 88px; margin-top: 6px; }
  .badge {
    position: absolute;
    top: 2450px;
    left: 560px;
    width: 150px;
    height: 150px;
    border-radius: 50%;
    background: var(--paper);
    border: 6px solid var(--brand-blue);
    display: flex;
    align-items: center;
    justify-content: center;
    text-align: center;
    font-weight: 700;
    font-size: 24px;
    line-height: 1.05;
    color: var(--brand-blue);
    transform: rotate(-25deg);
  }
  .visit-note {
    position: absolute;
    top: 2690px;
    right: 30px;
    font-weight: 500;
    font-style: italic;
    font-size: 38px;
    color: var(--ink);
  }
  .web-rule {
    position: absolute;
    top: 2748px;
    left: 0;
    width: 1200px;
    height: 8px;
    background: var(--ink);
  }
  .web-bar {
    position: absolute;
    top: 2768px;
    left: 0;
    width: 1200px;
    height: 125px;
    background: var(--ink);
    display: flex;
    align-items: center;
    justify-content: center;
    font-weight: 700;
    font-size: 106px;
    letter-spacing: 1px;
    color: var(--paper);
  }
</style>
</head>
<body>
  <main class="sign">
    <h1 class="headline">WHOLE<br>BODY</h1>
    <div class="banner">CRYOTHERAPY</div>

    <ul class="benefits">
      <li>Pain Management</li>
      <li class="alt">Injury Therapy</li>
      <li>Inflammatory Disorders</li>
      <li class="alt">Rapid Recovery</li>
      <li>Performance Enhancement</li>
      <li class="alt">Metabolic &amp; Immunity Boost</li>
      <li>Anti-Aging</li>
      <li class="alt">Skin Rejuvenation</li>
    </ul>

    <div class="unit-visual" role="img" aria-label="Photo of the whole body cryotherapy chamber with cold mist rising"></div>

    <div class="offer">
      <div class="just">JUST</div>
      <div class="count">
        <span class="digit">3</span>
        <span class="minutes">MINUTES</span>
        <span class="for">FOR</span>
      </div>
      <div class="tail">WHOLE BODY<br>RECOVERY</div>
    </div>

    <div class="badge">come inside<br>and ask<br>for details!</div>

    <p class="visit-note">...or visit:</p>
    <div class="web-rule"></div>
    <div class="web-bar">www.kelworthback.com</div>
  </main>
</body>
</html>
```